business card design for luxurious real estate brand

using the attached logo, i am looking for a 2-sided business card design. the back should be the gold logo on black background. the front needs to include: gold logo, name, phone, email, and website

Industry/Entity Type

real estate

Contact Information for Business Card

logo, name, email, phone, website

Font styles to use
Sans Serif

```html
<!DOCTYPE html>
<html lang="en">
<head>
<meta charset="utf-8">
<title>Casa Lumera – Business Card</title>
<link href="https://fonts.googleapis.com/css2?family=Montserrat:wght@300;400;500;700&display=swap" rel="stylesheet">
<style>
  :root {
    --backdrop: #959595;
    --card-dark: #222222;
    --card-dark-deep: #101010;
    --card-dark-light: #2e2e2e;
    --card-light: #ebebeb;
    --gold: #e8b90c;
    --ink: #333333;
    --ink-soft: #555555;
    --ink-muted: #7a7a7a;
  }
  * { margin: 0; padding: 0; box-sizing: border-box; }
  html, body {
    width: 1200px;
    height: 1000px;
    overflow: hidden;
    background: var(--backdrop);
    font-family: "Montserrat", sans-serif;
  }
  .canvas {
    position: relative;
    width: 1200px;
    height: 1000px;
  }
  .card {
    position: absolute;
    left: 293px;
    width: 615px;
    height: 350px;
    border-radius: 30px;
    overflow: hidden;
  }
  .card--back {
    top: 100px;
    background: var(--card-dark);
  }
  .card--front {
    top: 511px;
    background: var(--card-light);
  }
  .card__pattern {
    position: absolute;
    inset: 0;
    background: linear-gradient(90deg, var(--card-dark-deep) 0%, var(--card-dark) 50%, var(--card-dark-light) 100%);
  }
  .brand {
    position: absolute;
    display: flex;
    align-items: center;
    gap: 12px;
    color: var(--gold);
    font-weight: 500;
    letter-spacing: 3px;
    text-transform: uppercase;
    white-space: nowrap;
  }
  .brand__mark {
    width: 16px;
    height: 16px;
    background: var(--gold);
  }
  .card--back .brand {
    left: 278px;
    top: 262px;
    font-size: 19px;
  }
  .card--front .brand {
    left: 362px;
    top: 267px;
    font-size: 17px;
  }
  .person {
    position: absolute;
    left: 66px;
    top: 132px;
  }
  .person__name {
    font-weight: 700;
    font-size: 16px;
    letter-spacing: 3px;
    color: var(--ink);
    text-transform: uppercase;
    line-height: 20px;
  }
  .person__role {
    font-weight: 300;
    font-size: 16px;
    letter-spacing: 3px;
    color: var(--ink-soft);
    text-transform: uppercase;
    line-height: 20px;
  }
  .contact {
    position: absolute;
    left: 66px;
    top: 212px;
    list-style: none;
    font-size: 15px;
    font-weight: 400;
    color: var(--ink-muted);
    line-height: 28px;
  }
</style>
</head>
<body>
  <main class="canvas">
    <section class="card card--back">
      <div class="card__pattern" role="img" aria-label="Embossed repeating brand-mark pattern in dark tones"></div>
      <div class="brand"><span class="brand__mark"></span>Casa Lumera</div>
    </section>

    <section class="card card--front">
      <div class="person">
        <p class="person__name">Name Surname</p>
        <p class="person__role">Position</p>
      </div>
      <ul class="contact">
        <li>123-456-7890</li>
        <li>email@casalumera.com</li>
        <li>www.casalumera.com</li>
      </ul>
      <div class="brand"><span class="brand__mark"></span>Casa Lumera</div>
    </section>
  </main>
</body>
</html>
```